BrivaTrek Freight Services Business cards

Would like a very unique design catchy but professional for business cards. Please use log provided.Marlon WellsCeo and Founder TransCon Logistix Solutions1-888-913-3225mwells@tlsolutionsus.comwww.bfservicesco.com

```html
<!DOCTYPE html>
<html lang="en">
<head>
<meta charset="utf-8">
<title>BrivaTrek Freight Services – Business Cards</title>
<link rel="stylesheet" href="https://fonts.googleapis.com/css2?family=Roboto:wght@400;500;700&family=Roboto+Condensed:wght@700&display=swap">
<style>
  :root {
    --canvas-bg: #e9ecef;
    --card-white: #ffffff;
    --brand-blue: #1c78c4;
    --brand-deep: #0c58a6;
    --brand-sky: #6ccdf3;
    --brand-mid: #2f86d0;
    --back-blue: #4a8fd0;
    --back-mark: #1d5ea6;
    --accent-red: #e0262d;
    --text-dark: #111418;
    --text-sky: #2aa0da;
    --faint-mark: #3f74ad;
  }
  * { box-sizing: border-box; margin: 0; padding: 0; }
  html, body { width: 1200px; height: 1000px; overflow: hidden; }
  body {
    background: var(--canvas-bg);
    font-family: "Roboto", Arial, sans-serif;
    position: relative;
  }
  .card {
    position: absolute;
    left: 320px;
    width: 560px;
    height: 320px;
    border-radius: 22px;
    overflow: hidden;
    box-shadow: 0 6px 18px rgba(0,0,0,0.18);
  }
  .card--front { top: 120px; background: var(--card-white); }
  .card--back  { top: 560px; background: var(--back-blue); }

  .front-bands { position: absolute; inset: 0; }

  .brand-lockup {
    position: absolute;
    left: 26px;
    top: 24px;
    display: flex;
    align-items: center;
    gap: 8px;
  }
  .brand-lockup__square {
    width: 16px; height: 16px;
    background: var(--brand-deep);
  }
  .brand-lockup__name {
    font-family: "Roboto Condensed", Arial, sans-serif;
    font-weight: 700;
    font-size: 15px;
    color: var(--brand-deep);
  }

  .contact-list {
    position: absolute;
    left: 26px;
    top: 92px;
    list-style: none;
  }
  .contact-list__item {
    display: flex;
    align-items: center;
    gap: 10px;
    height: 30px;
    font-weight: 700;
    font-size: 15px;
    color: var(--text-dark);
  }
  .contact-list__icon { width: 22px; height: 22px; flex: none; }

  .front-company {
    position: absolute;
    left: 26px;
    bottom: 26px;
    font-weight: 500;
    font-size: 20px;
    color: var(--text-sky);
  }

  .person {
    position: absolute;
    right: 28px;
    top: 26px;
    text-align: right;
  }
  .person__name {
    font-weight: 700;
    font-size: 24px;
    letter-spacing: 1.5px;
    color: var(--text-dark);
  }
  .person__title {
    font-weight: 500;
    font-size: 13px;
    letter-spacing: 1px;
    color: var(--text-dark);
    margin-top: 4px;
  }

  .front-mark {
    position: absolute;
    left: 370px;
    top: 190px;
    width: 170px;
    font-family: "Roboto Condensed", Arial, sans-serif;
    font-weight: 700;
    font-size: 17px;
    text-align: center;
    color: var(--faint-mark);
  }

  .back-lockup {
    position: absolute;
    inset: 0;
    display: flex;
    align-items: center;
    justify-content: center;
    gap: 14px;
  }
  .back-lockup__square {
    width: 34px; height: 34px;
    background: var(--back-mark);
  }
  .back-lockup__name {
    font-family: "Roboto Condensed", Arial, sans-serif;
    font-weight: 700;
    font-size: 32px;
    color: var(--back-mark);
  }
</style>
</head>
<body>

  <section class="card card--front" aria-label="Business card front">
    <svg class="front-bands" viewBox="0 0 560 320" width="560" height="320" aria-hidden="true">
      <path d="M250,0 C330,80 340,220 296,320 L560,320 L560,0 Z" fill="var(--brand-sky)"/>
      <path d="M274,0 C356,86 362,222 320,320 L560,320 L560,0 Z" fill="var(--brand-deep)"/>
      <path d="M300,0 C382,90 388,222 346,320 L560,320 L560,0 Z" fill="var(--brand-mid)"/>
      <path d="M322,0 C404,92 408,224 370,320 L560,320 L560,0 Z" fill="var(--brand-blue)"/>
    </svg>

    <div class="brand-lockup">
      <span class="brand-lockup__square"></span>
      <span class="brand-lockup__name">BrivaTrek Freight Services</span>
    </div>

    <ul class="contact-list">
      <li class="contact-list__item">
        <svg class="contact-list__icon" viewBox="0 0 22 22" aria-hidden="true">
          <circle cx="11" cy="11" r="9.5" fill="#fff" stroke="var(--accent-red)" stroke-width="2"/>
          <path d="M7.5,6 C6.5,9.5 9.5,14.5 13.5,15.8 L15,14 L13,12.5 L12,13.5 C10.5,12.8 9.3,11.5 8.7,10 L9.7,9 L8.5,6.8 Z" fill="var(--brand-deep)"/>
        </svg>
        <span>1-888-472-6081</span>
      </li>
      <li class="contact-list__item">
        <svg class="contact-list__icon" viewBox="0 0 22 22" aria-hidden="true">
          <circle cx="11" cy="11" r="9.5" fill="var(--brand-blue)" stroke="var(--accent-red)" stroke-width="2"/>
          <rect x="6" y="7.5" width="10" height="7" fill="#fff"/>
          <path d="M6,7.5 L11,11.5 L16,7.5" fill="none" stroke="var(--brand-deep)" stroke-width="1"/>
        </svg>
        <span>dharrow@bfservicesco.com</span>
      </li>
      <li class="contact-list__item">
        <svg class="contact-list__icon" viewBox="0 0 22 22" aria-hidden="true">
          <circle cx="11" cy="11" r="9.5" fill="var(--brand-blue)" stroke="var(--accent-red)" stroke-width="2"/>
          <circle cx="11" cy="11" r="5" fill="none" stroke="#fff" stroke-width="1.2"/>
          <ellipse cx="11" cy="11" rx="2.2" ry="5" fill="none" stroke="#fff" stroke-width="1"/>
          <line x1="6" y1="11" x2="16" y2="11" stroke="#fff" stroke-width="1"/>
        </svg>
        <span>www.bfservicesco.com</span>
      </li>
    </ul>

    <p class="front-company">BrivaTrek Freight Services</p>

    <div class="person">
      <p class="person__name">Dustin Harrow</p>
      <p class="person__title">Ceo and Founder</p>
    </div>

    <p class="front-mark">BrivaTrek Freight Services</p>
  </section>

  <section class="card card--back" aria-label="Business card back">
    <div class="back-lockup">
      <span class="back-lockup__square"></span>
      <span class="back-lockup__name">BrivaTrek Freight Services</span>
    </div>
  </section>

</body>
</html>
```